Business Card For Kelmora Financial Consulting

Hi, I would like a business card designed. Bold, modern.
Please use the same design as the logo. I have also attached the website design to see the overall theme.
Wordmark Font
Color: Hex: #01AEF7

```html
<!DOCTYPE html>
<html lang="en">
<head>
<meta charset="utf-8">
<title>Kelmora Financial Consulting — Business Card</title>
<link href="https://fonts.googleapis.com/css2?family=Lato:wght@400;700;900&display=swap" rel="stylesheet">
<style>
  :root {
    --stage: #2a2a2a;
    --card: #18232d;
    --card-edge: #1d2a35;
    --brand-blue: #01aef7;
    --ink-light: #ffffff;
    --ink-soft: #d8e2ea;
  }
  * { box-sizing: border-box; margin: 0; padding: 0; }
  html, body {
    width: 1200px; height: 875px; overflow: hidden;
    background: var(--stage);
    font-family: "Lato", Arial, sans-serif;
  }
  .sheet {
    width: 1200px; height: 875px;
    display: flex; align-items: center; justify-content: center; gap: 40px;
  }
  .card {
    position: relative;
    width: 540px; height: 309px;
    background: var(--card);
    overflow: hidden;
    box-shadow: 0 18px 40px rgba(0,0,0,0.45);
  }

  /* Front */
  .card-front { display: flex; align-items: center; justify-content: center; }
  .wordmark { display: flex; align-items: center; gap: 18px; }
  .wordmark-square {
    width: 64px; height: 64px;
    border: 5px solid var(--brand-blue);
  }
  .wordmark-text {
    color: var(--ink-light); font-weight: 900; line-height: 1;
  }
  .wordmark-name { display: block; font-size: 56px; letter-spacing: 2px; }
  .wordmark-sub { display: block; font-size: 16px; letter-spacing: 17.5px; margin-top: 8px; }

  /* Back */
  .card-back .wordmark { position: absolute; right: 34px; top: 46px; gap: 10px; }
  .card-back .wordmark-square { width: 38px; height: 38px; border-width: 3px; }
  .card-back .wordmark-name { font-size: 33px; letter-spacing: 1px; }
  .card-back .wordmark-sub { font-size: 9.5px; letter-spacing: 10.4px; margin-top: 5px; }

  .accent-rule {
    position: absolute; left: 290px; right: 0; top: 177px;
    height: 2px; background: var(--brand-blue);
  }
  .name-band { position: absolute; left: 0; top: 150px; }
  .person {
    position: absolute; left: 34px; top: 156px; color: var(--ink-light);
  }
  .person-name { font-weight: 900; font-size: 25px; letter-spacing: 0.5px; line-height: 1.1; }
  .person-role { font-weight: 400; font-size: 14px; margin-top: 1px; }

  .contact-list {
    position: absolute; left: 34px; top: 226px;
    list-style: none; color: var(--ink-light); font-size: 13px;
  }
  .contact-list li { display: flex; align-items: center; gap: 9px; height: 18px; }
  .contact-list svg { width: 11px; height: 11px; fill: var(--brand-blue); flex: none; }

  .company-block {
    position: absolute; right: 30px; top: 194px;
    text-align: right; color: var(--ink-soft); font-size: 12.5px; line-height: 1.4;
  }
  .company-name { color: var(--ink-light); font-weight: 700; }
  .company-web { color: var(--brand-blue); font-size: 13px; }
</style>
</head>
<body>
<main class="sheet">

  <section class="card card-front" aria-label="Card front">
    <div class="wordmark">
      <span class="wordmark-square" aria-hidden="true"></span>
      <span class="wordmark-text">
        <span class="wordmark-name">KELMORA</span>
        <span class="wordmark-sub">CONSULTING</span>
      </span>
    </div>
  </section>

  <section class="card card-back" aria-label="Card back">
    <div class="wordmark">
      <span class="wordmark-square" aria-hidden="true"></span>
      <span class="wordmark-text">
        <span class="wordmark-name">KELMORA</span>
        <span class="wordmark-sub">CONSULTING</span>
      </span>
    </div>

    <div class="accent-rule"></div>
    <svg class="name-band" width="300" height="66" viewBox="0 0 300 66" aria-hidden="true">
      <polygon points="0,0 240,0 292,28 292,66 0,66" fill="#01aef7"/>
    </svg>

    <div class="person">
      <p class="person-name">DANIEL HARROW</p>
      <p class="person-role">Founder &amp; CEO</p>
    </div>

    <ul class="contact-list">
      <li><svg viewBox="0 0 24 24" aria-hidden="true"><path d="M6.6 10.8a15.1 15.1 0 0 0 6.6 6.6l2.2-2.2a1 1 0 0 1 1-.25 11.4 11.4 0 0 0 3.6.57 1 1 0 0 1 1 1V20a1 1 0 0 1-1 1A17 17 0 0 1 3 4a1 1 0 0 1 1-1h3.5a1 1 0 0 1 1 1c0 1.25.2 2.45.57 3.6a1 1 0 0 1-.25 1z"/></svg>(555) 014-2290</li>
      <li><svg viewBox="0 0 24 24" aria-hidden="true"><path d="M7 1h10a2 2 0 0 1 2 2v18a2 2 0 0 1-2 2H7a2 2 0 0 1-2-2V3a2 2 0 0 1 2-2zm0 3v14h10V4zm5 15.5a1.2 1.2 0 1 0 0 2.4 1.2 1.2 0 0 0 0-2.4z"/></svg>(555) 017-3381</li>
      <li><svg viewBox="0 0 24 24" aria-hidden="true"><path d="M6 2h10v5H6zM3 8h18a1 1 0 0 1 1 1v9h-4v4H6v-4H2V9a1 1 0 0 1 1-1zm5 7v5h8v-5z"/></svg>(555) 019-4472</li>
      <li><svg viewBox="0 0 24 24" aria-hidden="true"><path d="M2 5h20v14H2zm2 2v.5l8 5 8-5V7z"/></svg>info@kelmoraconsulting.com</li>
    </ul>

    <address class="company-block" style="font-style: normal;">
      <p class="company-name">Kelmora Consulting Ltd</p>
      <p>Your Address, City</p>
      <p>State, Zip 1235</p>
      <p class="company-web">KelmoraConsulting.com</p>
    </address>
  </section>

</main>
</body>
</html>
```